Business Card Design Project

Attached is a rough business card design. We like this general design but we feel that the layout, text, color can use improvement and we seek the help of a professional designer.
We have a television and film production company based in New York. We need our cards for television network executives, other production executives, financiers etc. We deal with creative types as well as business people so we need the card to be interesting and edgy just like the name of our company - KICKTHEDOOR. The design should reflect the edgy, punk rock attitude of our company.
We prefer orange typeface for the logo but we're open to other ideas. I am attaching our existing business card and other files to help with the design.
Thank you in advance!!
Updates
Target Market(s)
Television and film producers, television network executives, other production executives, financiers, distribution companies
Industry/Entity Type
Film Production
Requirements
Must have
- I am attaching a photo of the company mascot which is a dog. We prefer to have the dog's photo as part of the card but we're open to the other ideas.
Name, phone number, email

```html
<!DOCTYPE html>
<html lang="en">
<head>
<meta charset="utf-8">
<title>Kickthedoor – Business Card</title>
<link href="https://fonts.googleapis.com/css2?family=Questrial&display=swap" rel="stylesheet">
<style>
  :root {
    --card-dark: #121415;
    --card-mid: #1d2122;
    --brand-red: #e2221c;
    --label-red: #c9241f;
    --name-grey: #d9dcdc;
    --detail-grey: #c4c8c8;
    --frame-pink: #f1dcdc;
    --frame-white: #f7eeee;
    --glow-teal: rgba(63, 194, 180, 0.22);
    --glow-green: rgba(47, 138, 74, 0.22);
    --glow-violet: rgba(122, 106, 208, 0.16);
  }
  * { margin: 0; padding: 0; box-sizing: border-box; }
  html, body {
    width: 1200px; height: 741px; overflow: hidden;
    background: var(--card-dark);
  }
  .card {
    position: relative; width: 1200px; height: 741px; overflow: hidden;
    background: radial-gradient(ellipse at 30% 40%, var(--card-mid) 0%, var(--card-dark) 70%);
    font-family: "Questrial", "Century Gothic", sans-serif;
  }
  .card__glow {
    position: absolute; inset: 0;
    background:
      radial-gradient(ellipse 160px 420px at 1010px 300px, var(--glow-teal), transparent 70%),
      radial-gradient(ellipse 130px 300px at 1080px 520px, var(--glow-violet), transparent 70%),
      radial-gradient(ellipse 620px 110px at 560px 690px, var(--glow-green), transparent 70%);
    filter: blur(12px);
  }
  .mascot {
    position: absolute; left: 700px; top: 20px; width: 420px; height: 260px;
  }
  .mascot__frame {
    position: absolute; inset: 0;
    background: var(--frame-pink); opacity: 0.85;
  }
  .mascot__frame--back { transform: rotate(-14deg) translate(-20px, 30px); opacity: 0.55; background: var(--frame-white); }
  .mascot__frame--mid { transform: rotate(-7deg) translate(-6px, 14px); opacity: 0.7; }
  .mascot__photo {
    position: absolute; inset: 12px 16px;
    background:
      radial-gradient(ellipse at 48% 48%, #b9704c 0%, #9a5a3c 28%, transparent 52%),
      linear-gradient(180deg, #d7a9a6 0%, #e9c8c3 45%, #f2e3df 100%);
  }
  .brand {
    position: absolute; left: 70px; top: 268px;
    font-size: 88px; line-height: 1; color: var(--brand-red); letter-spacing: 1px;
  }
  .person {
    position: absolute; left: 74px; top: 385px;
    font-size: 66px; line-height: 1; color: var(--name-grey); letter-spacing: 1px;
  }
  .contact { position: absolute; left: 78px; top: 478px; list-style: none; }
  .contact__row { display: flex; align-items: baseline; height: 52px; }
  .contact__label { width: 100px; font-size: 24px; color: var(--label-red); }
  .contact__value { font-size: 34px; color: var(--detail-grey); }
</style>
</head>
<body>
  <div class="card">
    <div class="card__glow" role="img" aria-label="Soft teal, violet and green light ribbons sweeping across the card"></div>

    <div class="mascot">
      <div class="mascot__frame mascot__frame--back"></div>
      <div class="mascot__frame mascot__frame--mid"></div>
      <div class="mascot__frame"></div>
      <div class="mascot__photo" role="img" aria-label="Photo of the company mascot, a dog lying on the floor with a small ball"></div>
    </div>

    <div class="brand">Kickthedoor</div>
    <div class="person">Daniel Morrow</div>
    <ul class="contact">
      <li class="contact__row"><span class="contact__label">Phone :</span><span class="contact__value">917-555-0183</span></li>
      <li class="contact__row"><span class="contact__label">Email :</span><span class="contact__value">daniel@kickthedoor.com</span></li>
    </ul>
  </div>
</body>
</html>
```